Hollerby Consulting needs a quality & professional business card!

I am a recruitment and employment consultant from Brisbane, Australia and I had a fantastic logo organised by this community to I am hoping the business card will be the same.

I have attached the Hollerby consulting logo that ideally would feature on the back of the business card. There are a number of logos for you to use as you see fit. I would like the colour cheme to match that of the Hollerby Consulting logo. I also have a secondary company called Career Lantern Australia and I have included that logo as well. While it is an important part of the business I don't want this logo feature too predominantly as I am moving out of this space. This logo was created by myself and is of low quality. Feel free to use the icon and words however you want. The winning design will be smart, professional and eye-catching.

The information I am looking for in the business card is:
Name: Derek Hollerby
Position: Founder & Director
Phone: (07) 3156 4082
Mobile: 0418 672 051
Email: derek@careerlantern-example.com.au

Target Market(s)

Recruiters, government, large companies

Contact Information for Business Card

Name: Derek Hollerby
Phone: (07) 3156 4082
Mobile: 0418 672 051
Web: www.careerlantern-example.com.au

Font styles to use
Serif
Sans Serif

Requirements
Must have
• Hollerby Consulting Logo on reverse side
• Contact details on front side with smaller reference to Hollerby Consulting logo and Career Lantern Australia logo

```html
<!DOCTYPE html>
<html lang="en">
<head>
<meta charset="utf-8">
<title>Hollerby Consulting – Business Card</title>
<link rel="stylesheet" href="https://fonts.googleapis.com/css2?family=Montserrat:wght@400;500;600&display=swap">
<style>
  :root {
    --backdrop: #2b2d30;
    --card-dark: #25272a;
    --card-white: #ffffff;
    --brand-blue: #1b9ad6;
    --brand-green: #00b050;
    --brand-orange: #e8812f;
    --text-light: #f2f2f2;
    --text-grey: #b9bcc0;
  }
  * { box-sizing: border-box; margin: 0; padding: 0; }
  html, body {
    width: 1200px; height: 900px; overflow: hidden;
    background: var(--backdrop);
    font-family: "Montserrat", Arial, sans-serif;
  }
  .canvas { position: relative; width: 1200px; height: 900px; }

  .card {
    position: absolute;
    width: 580px; height: 330px;
    border-radius: 22px;
    overflow: hidden;
    box-shadow: 0 14px 30px rgba(0,0,0,.45);
  }

  /* Front */
  .card-front { left: 40px; top: 470px; background: var(--card-white); }
  .front-panel {
    position: absolute; left: 0; top: 0; width: 330px; height: 100%;
    background: var(--card-dark);
    padding: 34px 0 0 34px;
  }
  .person-name {
    color: var(--brand-blue); font-weight: 500; font-size: 25px;
    letter-spacing: .5px; text-transform: uppercase;
  }
  .person-role { color: var(--text-light); font-size: 14px; margin-top: 4px; }
  .name-rule { width: 20px; height: 2px; background: var(--brand-blue); margin: 30px 0 34px; }
  .contact-list { list-style: none; }
  .contact-item {
    display: flex; align-items: center; gap: 12px;
    color: var(--text-light); font-size: 14px; margin-bottom: 12px;
  }
  .contact-icon { width: 24px; height: 24px; flex: none; }

  .front-block { position: absolute; }
  .block-green { right: 0; top: 0; width: 170px; height: 115px; background: var(--brand-green); }
  .block-orange { left: 330px; bottom: 0; width: 150px; height: 85px; background: var(--brand-orange); }
  .location-tag { position: absolute; left: 312px; top: 122px; width: 40px; height: 40px; }
  .front-brand {
    position: absolute; left: 370px; top: 140px;
    display: flex; align-items: center; gap: 10px;
    color: var(--card-dark); font-size: 15px; font-weight: 500; line-height: 1.25;
    text-transform: uppercase; letter-spacing: 1px;
  }
  .brand-dot { width: 14px; height: 14px; border-radius: 50%; background: var(--brand-blue); flex: none; }

  /* Back */
  .card-back {
    left: 580px; top: 90px;
    background: linear-gradient(160deg, #2e3033 0%, var(--card-dark) 60%, #1e2022 100%);
    display: flex; align-items: center; justify-content: center;
  }
  .back-brand {
    display: flex; align-items: center; gap: 18px;
    color: var(--text-grey); font-weight: 500; font-size: 34px;
    letter-spacing: 3px; text-transform: uppercase; line-height: 1.2;
  }
  .back-brand .brand-square { width: 26px; height: 26px; background: var(--text-grey); flex: none; }
</style>
</head>
<body>
<main class="canvas">

  <section class="card card-back" aria-label="Card reverse">
    <div class="back-brand">
      <span class="brand-square"></span>
      <span>Hollerby<br>Consulting</span>
    </div>
  </section>

  <section class="card card-front" aria-label="Card front">
    <div class="front-panel">
      <h1 class="person-name">Derek Hollerby</h1>
      <p class="person-role">Founder &amp; Director</p>
      <div class="name-rule"></div>
      <ul class="contact-list">
        <li class="contact-item">
          <svg class="contact-icon" viewBox="0 0 24 24"><circle cx="12" cy="12" r="12" fill="#1b9ad6"/><path d="M8 7c1-1 2 0 2.5 1.5s-.5 2-1 2.5c.8 1.6 1.9 2.7 3.5 3.5.5-.5 1-1.5 2.5-1s2.5 1.5 1.5 2.5c-1.5 1.5-4 1-6.5-1.5S6.5 8.5 8 7z" fill="#fff"/></svg>
          (07) 3156 4082
        </li>
        <li class="contact-item">
          <svg class="contact-icon" viewBox="0 0 24 24"><circle cx="12" cy="12" r="12" fill="#1b9ad6"/><rect x="8.5" y="5.5" width="7" height="13" rx="1.2" fill="#fff"/><rect x="9.7" y="7.2" width="4.6" height="8.5" fill="#1b9ad6"/></svg>
          0418 672 051
        </li>
        <li class="contact-item">
          <svg class="contact-icon" viewBox="0 0 24 24"><circle cx="12" cy="12" r="12" fill="#1b9ad6"/><rect x="6" y="8" width="12" height="8.5" fill="#fff"/><path d="M6 8l6 5 6-5" fill="none" stroke="#1b9ad6" stroke-width="1.2"/></svg>
          derek@careerlantern-example.com.au
        </li>
      </ul>
    </div>

    <div class="front-block block-green"></div>
    <div class="front-block block-orange"></div>

    <svg class="location-tag" viewBox="0 0 40 40" aria-hidden="true">
      <path d="M4 8h22l10 12-10 12H4z" fill="#fff" stroke="#1b9ad6" stroke-width="1.5"/>
      <path d="M18 12a6 6 0 0 1 6 6c0 4-6 10-6 10s-6-6-6-10a6 6 0 0 1 6-6z" fill="#25272a"/>
      <circle cx="18" cy="18" r="2.3" fill="#fff"/>
    </svg>

    <div class="front-brand">
      <span class="brand-dot"></span>
      <span>Hollerby<br>Consulting</span>
    </div>
  </section>

</main>
</body>
</html>
```